Commercial Construction Company

We need a business card design based on our current logo. We are a commercial general contractor based in Southern California that specializes in bank remodels. We would like to see designs that incorporate dark blue. The final design should portray an image of professionalism and quality.

If possible, I would like to add metallic foil to the design. Thank you

```html
<!DOCTYPE html>
<html lang="en">
<head>
<meta charset="utf-8">
<title>Harlow Commercial Builders – Business Card</title>
<link href="https://fonts.googleapis.com/css2?family=Open+Sans:wght@400;600;700&display=swap" rel="stylesheet">
<style>
  :root {
    --backdrop: #dcdcda;
    --card: #222223;
    --navy: #1d4f8c;
    --navy-bright: #2a62a8;
    --silver: #c8c8c8;
    --white: #f4f4f4;
    --muted: #8a8a8a;
  }
  * { margin: 0; padding: 0; box-sizing: border-box; }
  html, body {
    width: 1200px; height: 801px; overflow: hidden;
    background: var(--backdrop);
    font-family: "Open Sans", Arial, sans-serif;
  }
  .sheet {
    position: relative; width: 1200px; height: 801px;
    display: flex; align-items: center; justify-content: center; gap: 40px;
  }
  .card {
    position: relative; width: 540px; height: 309px;
    background: var(--card);
    border-bottom: 3px solid var(--navy);
    box-shadow: 0 10px 24px rgba(0,0,0,.22);
  }
  /* front */
  .card-front { display: flex; }
  .front-brand {
    width: 300px; display: flex; align-items: center; justify-content: center; gap: 12px;
  }
  .brand-dot {
    width: 22px; height: 22px; border-radius: 50%; background: var(--navy);
  }
  .brand-name {
    color: var(--white); font-weight: 700; font-size: 21px; line-height: 1.15;
    text-transform: uppercase; letter-spacing: .5px;
  }
  .front-divider {
    width: 1px; margin: 58px 0; background: var(--navy);
  }
  .front-details {
    flex: 1; padding: 62px 0 0 26px; color: var(--white);
  }
  .person-name {
    color: var(--navy-bright); font-weight: 700; font-size: 17px;
    text-transform: uppercase; letter-spacing: .3px;
  }
  .person-title { color: var(--muted); font-size: 12.5px; margin-bottom: 10px; }
  .address { font-size: 12.5px; line-height: 1.45; margin-bottom: 8px; }
  .contact-list { list-style: none; font-size: 12.5px; line-height: 1.55; }
  .contact-list li { display: flex; align-items: center; gap: 8px; }
  .contact-list svg { width: 10px; height: 10px; fill: var(--navy-bright); flex: none; }
  /* back */
  .card-back { display: flex; align-items: center; justify-content: center; }
  .back-name {
    color: var(--silver); font-weight: 700; font-size: 30px;
    text-transform: uppercase; letter-spacing: 1px; text-align: center; line-height: 1.15;
  }
</style>
</head>
<body>
<main class="sheet">
  <section class="card card-front">
    <div class="front-brand">
      <span class="brand-dot"></span>
      <span class="brand-name">Harlow<br>Commercial<br>Builders</span>
    </div>
    <div class="front-divider"></div>
    <div class="front-details">
      <p class="person-name">Carl Renner</p>
      <p class="person-title">President</p>
      <p class="address">1180 Marina Vista Drive<br>Seal Beach CA 90740</p>
      <ul class="contact-list">
        <li><svg viewBox="0 0 10 10"><path d="M2 0.5l2 2-1 1.2c.6 1.3 1.8 2.5 3.1 3.1l1.2-1 2 2-1.3 1.7C4.2 9.3.7 5.8.3 1.8z"/></svg>555-013-2748</li>
        <li><svg viewBox="0 0 10 10"><path d="M2.5 0h5v10h-5zM3.3 1v7h3.4V1z"/></svg>555-013-2749</li>
        <li><svg viewBox="0 0 10 10"><path d="M0 2h10v6H0zM.8 2.6L5 5.6l4.2-3z" fill-rule="evenodd"/></svg>office@harlowbuild.com</li>
        <li><svg viewBox="0 0 10 10"><circle cx="5" cy="5" r="4.6"/></svg>www.harlowbuild.com</li>
      </ul>
    </div>
  </section>
  <section class="card card-back">
    <span class="back-name">Harlow<br>Commercial Builders</span>
  </section>
</main>
</body>
</html>
```